Vell Partners Building Business Cards

We need a business card that reflects our business as "Solar Experts" in San Diego. Browse our website www.vellpartners.example our License needs to be displayed as "CSLB# 4718392" our phone number is (619) 555-0147

Save thousands on your electric bills and increase the value of your home while helping to protect the environment. Our solar installation experts will help you design the system that's right for you, using only the highest quality equipment that will look great and give you ideal performance. Our goal is to make you energy independent, and get your electric bill to 0.

Tobias Wrenfield
(619) 555-0147
tobias@vellpartners.example

Target Market(s)

Home owners in san diego looking for solar

Industry/Entity Type

Solar Energy

Contact Information for Business Card

Tobias Wrenfield
(619) 555-0147
tobias@vellpartners.example

Font styles to use
Other font styles liked:
• Use our logo font

Requirements
Must have
• License needs to be displayed as "CSLB# 4718392" our phone number is (619) 555-0147
Nice to have
• Real images of rooftop home solar in san diego
Should not have
• our business address

```html
<!DOCTYPE html>
<html lang="en">
<head>
<meta charset="utf-8">
<title>Vell Partners Building – Business Card</title>
<link rel="stylesheet" href="https://fonts.googleapis.com/css2?family=Montserrat:wght@700;800&family=Cinzel:wght@400;600&display=swap">
<style>
  :root {
    --backdrop: #1c1d20;
    --card-blue: #174a86;
    --gold: #f6b11c;
    --white: #ffffff;
    --ink-blue: #173f72;
    --photo-sky: #5f8fc4;
    --photo-panel: #1f3570;
    --photo-roof: #8d8577;
  }
  * { margin: 0; padding: 0; box-sizing: border-box; }
  html, body { width: 1200px; height: 900px; overflow: hidden; }
  body {
    background: var(--backdrop);
    position: relative;
    font-family: "Cinzel", serif;
  }
  .card {
    position: absolute;
    width: 700px;
    height: 400px;
    border-radius: 4px;
    overflow: hidden;
    box-shadow: 0 18px 40px rgba(0,0,0,.55);
  }

  /* Front */
  .card-front { left: 100px; top: 50px; }
  .front-photo {
    position: absolute; inset: 0;
    background:
      linear-gradient(160deg, rgba(95,143,196,.85) 0%, rgba(31,53,112,.9) 35%, rgba(31,53,112,.95) 65%, rgba(141,133,119,.9) 100%);
  }
  .front-shade {
    position: absolute; inset: 0;
    background: linear-gradient(180deg, rgba(0,0,0,0) 40%, rgba(0,0,0,.35) 100%);
  }
  .front-name {
    position: absolute;
    left: 60px; top: 150px;
    font-family: "Montserrat", sans-serif;
    font-weight: 800;
    font-size: 52px;
    line-height: 1.05;
    letter-spacing: -1px;
    color: var(--white);
    width: 560px;
  }
  .front-web {
    position: absolute;
    right: 60px; bottom: 40px;
    font-size: 17px;
    letter-spacing: 1px;
    color: var(--white);
    text-transform: uppercase;
  }

  /* Back */
  .card-back { left: 400px; top: 450px; background: var(--card-blue); }
  .brand-mark {
    position: absolute;
    left: 44px; top: 150px;
    display: flex; align-items: center; gap: 14px;
  }
  .brand-dot {
    width: 56px; height: 56px; border-radius: 50%;
    background: var(--gold);
    flex: none;
  }
  .brand-name {
    font-family: "Montserrat", sans-serif;
    font-weight: 700;
    font-size: 24px;
    line-height: 1.15;
    color: var(--white);
    width: 170px;
  }
  .contact {
    position: absolute;
    left: 330px; top: 92px;
    padding-left: 20px;
    border-left: 2px solid var(--gold);
  }
  .contact-name {
    font-family: "Montserrat", sans-serif;
    font-weight: 700;
    font-size: 27px;
    color: var(--white);
    margin-bottom: 10px;
  }
  .contact-line {
    display: flex; align-items: center; gap: 10px;
    font-size: 15px;
    letter-spacing: .5px;
    color: var(--white);
    text-transform: uppercase;
    margin-bottom: 6px;
  }
  .contact-line svg { width: 13px; height: 13px; flex: none; }
  .gold-rule {
    position: absolute;
    top: 340px;
    height: 2px;
    background: var(--gold);
  }
  .gold-rule.left { left: 0; width: 316px; }
  .gold-rule.right { left: 500px; right: 0; }
  .license {
    position: absolute;
    left: 326px; top: 322px;
    width: 164px; height: 36px;
    border-radius: 10px;
    background: var(--white);
    color: var(--ink-blue);
    font-size: 17px;
    font-weight: 600;
    display: flex; align-items: center; justify-content: center;
  }
</style>
</head>
<body>

  <section class="card card-front">
    <div class="front-photo" role="img" aria-label="Photo of solar panels installed on a tiled San Diego home rooftop under a blue sky"></div>
    <div class="front-shade"></div>
    <div class="front-name">Vell Partners Building</div>
    <div class="front-web">www.vellpartners.example</div>
  </section>

  <section class="card card-back">
    <div class="brand-mark">
      <span class="brand-dot"></span>
      <span class="brand-name">Vell Partners Building</span>
    </div>

    <div class="contact">
      <div class="contact-name">Tobias Wrenfield</div>
      <div class="contact-line">
        <svg viewBox="0 0 24 24" aria-hidden="true"><path fill="#f6b11c" d="M6.6 10.8a15.1 15.1 0 0 0 6.6 6.6l2.2-2.2c.3-.3.7-.4 1-.2 1.1.4 2.3.6 3.6.6.6 0 1 .4 1 1V20c0 .6-.4 1-1 1A17 17 0 0 1 3 4c0-.6.4-1 1-1h3.5c.6 0 1 .4 1 1 0 1.3.2 2.5.6 3.6.1.3 0 .7-.2 1z"/></svg>
        <span>(619) 555-0147</span>
      </div>
      <div class="contact-line">
        <svg viewBox="0 0 24 24" aria-hidden="true"><rect x="2" y="5" width="20" height="14" rx="2" fill="none" stroke="#f6b11c" stroke-width="2.5"/><path d="M3 6l9 7 9-7" fill="none" stroke="#f6b11c" stroke-width="2.5"/></svg>
        <span>tobias@vellpartners.example</span>
      </div>
      <div class="contact-line">
        <svg viewBox="0 0 24 24" aria-hidden="true"><circle cx="12" cy="12" r="9.5" fill="none" stroke="#f6b11c" stroke-width="2.5"/><path d="M2.5 12h19M12 2.5c3 3 3 16 0 19M12 2.5c-3 3-3 16 0 19" fill="none" stroke="#f6b11c" stroke-width="2"/></svg>
        <span>www.vellpartners.example</span>
      </div>
    </div>

    <div class="gold-rule left"></div>
    <div class="license">CSLB# 4718392</div>
    <div class="gold-rule right"></div>
  </section>

</body>
</html>
```